Real Estate Managemene Company Needs Business Card Design

We have a logo design and just need business cards made now for our business. Please use PDF logo # 3.

Card with Information to be attached shortly.

The card is used for a real estate management company. We will need to add four other employees and their cards.

Industry/Entity Type

Real Estate

Contact Information for Business Card

Tariq Hamdan
President
3187 Thornwick Avenue
Suite C
Glendale Heights, IL 60152
Phone 630.417.2286
Fax 630.417.2287
Cell 630.473.8062
vantorp@mailbreeze.net

Once design is approved we will have four other employees
Omar Hamdan
Operations Manager

Nadia Hamdan
Administrative Manager

Faz Hamdan
Principal

We would need to take out the cell # 630.473.8062 out for the remaining three cards.

Requirements
Must have
• Please use logo attached

```html
<!DOCTYPE html>
<html lang="en">
<head>
<meta charset="utf-8">
<title>Business Card – Tariq Hamdan</title>
<link rel="stylesheet" href="https://fonts.googleapis.com/css2?family=Lato:wght@300;400;700&display=swap">
<style>
  :root {
    --backdrop: #3e3e40;
    --card: #ffffff;
    --brand-blue: #0b5789;
    --body-grey: #6a6a6a;
  }
  * { margin: 0; padding: 0; box-sizing: border-box; }
  html, body {
    width: 1200px; height: 1200px; overflow: hidden;
    background: var(--backdrop);
    font-family: "Lato", "Gill Sans", sans-serif;
  }
  .card {
    position: absolute;
    left: 210px; top: 344px;
    width: 782px; height: 513px;
    background: var(--card);
  }
  .edge-rule {
    position: absolute; top: 0; bottom: 0;
    left: 736px; width: 5px;
    background: var(--brand-blue);
  }
  .edge-band {
    position: absolute; top: 0; bottom: 0;
    left: 746px; right: 0;
    background: var(--brand-blue);
  }
  .brand {
    position: absolute;
    left: 69px; top: 100px;
    display: flex; align-items: center; gap: 16px;
  }
  .brand-mark {
    width: 54px; height: 54px;
    background: var(--brand-blue);
  }
  .brand-name {
    color: var(--brand-blue);
    font-weight: 700;
    font-size: 24px;
    line-height: 1.15;
    letter-spacing: 0.3px;
  }
  .person {
    position: absolute;
    left: 70px; top: 268px;
    color: var(--brand-blue);
  }
  .person-name { font-size: 24px; font-weight: 700; line-height: 1.1; }
  .person-title { font-size: 21px; font-weight: 300; margin-top: 3px; }
  .contact-list {
    position: absolute;
    left: 246px; top: 268px;
    list-style: none;
    color: var(--body-grey);
    font-size: 21px; font-weight: 300;
  }
  .contact-item {
    display: flex; align-items: flex-start;
    height: 34px; line-height: 26px;
  }
  .contact-item.address { margin-top: 6px; line-height: 26px; height: auto; }
  .contact-icon {
    width: 17px; height: 17px;
    margin: 4px 13px 0 0;
    fill: var(--brand-blue);
    flex: none;
  }
</style>
</head>
<body>
  <div class="card">
    <div class="brand">
      <div class="brand-mark"></div>
      <div class="brand-name">Northgate Realty<br>Management Group</div>
    </div>

    <div class="person">
      <div class="person-name">Tariq Hamdan</div>
      <div class="person-title">President</div>
    </div>

    <ul class="contact-list">
      <li class="contact-item">
        <svg class="contact-icon" viewBox="0 0 24 24"><path d="M6.6 10.8a15 15 0 0 0 6.6 6.6l2.2-2.2c.3-.3.7-.4 1-.2 1.1.4 2.3.6 3.6.6.6 0 1 .4 1 1V20c0 .6-.4 1-1 1A17 17 0 0 1 3 4c0-.6.4-1 1-1h3.5c.6 0 1 .4 1 1 0 1.3.2 2.5.6 3.6.1.3 0 .7-.2 1z"/></svg>
        <span>630.417.2286</span>
      </li>
      <li class="contact-item">
        <svg class="contact-icon" viewBox="0 0 24 24"><path d="M2 8h4v13H2zM7 4h10v4H7zM7 9h15v12H7zm3 3v2h2v-2zm4 0v2h2v-2zm4 0v2h2v-2zm-8 4v2h2v-2zm4 0v2h2v-2zm4 0v2h2v-2z"/></svg>
        <span>630.417.2287</span>
      </li>
      <li class="contact-item">
        <svg class="contact-icon" viewBox="0 0 24 24"><path d="M7 2h10a1 1 0 0 1 1 1v18a1 1 0 0 1-1 1H7a1 1 0 0 1-1-1V3a1 1 0 0 1 1-1zm1 3v12h8V5zm4 13.5a1 1 0 1 0 0 2 1 1 0 0 0 0-2z"/></svg>
        <span>630.473.8062</span>
      </li>
      <li class="contact-item">
        <svg class="contact-icon" viewBox="0 0 24 24"><path d="M2 6h20v1l-10 6L2 7zm0 3l10 6 10-6v9H2z"/></svg>
        <span>vantorp@mailbreeze.net</span>
      </li>
      <li class="contact-item address">
        <svg class="contact-icon" viewBox="0 0 24 24"><path d="M12 1a8 8 0 0 0-8 8c0 6 8 14 8 14s8-8 8-14a8 8 0 0 0-8-8zm0 11a3 3 0 1 1 0-6 3 3 0 0 1 0 6z"/></svg>
        <span>3187 Thornwick Avenue<br>Suite C Brookmere Falls, IL 60152</span>
      </li>
    </ul>

    <div class="edge-rule"></div>
    <div class="edge-band"></div>
  </div>
</body>
</html>
```